Investment Group needs a web page design

We need a web page design for a San Francisco-based investment group called 'Valtrimor LLC'. The final design should be stylish and attractive to the idea while retaining a sense of stability and professionalism. A great example is http://brindlewoodholdings.com/.

I am attaching the group's logo which should be the base for the webpage design.
Updates

Please note that I am interested in a single webpage that presents basic information. See the following example: http://brindlewoodholdings.com/

Target Market(s)

persons doing initial due diligence and trying to assess what kind of group we are.

Industry/Entity Type

Investment

Font styles to use
Serif

Colors
86acd3
3176b5
0355a3

Requirements
Nice to have
• Would love the design to incorporate the concept - 'Sen no Sen: a block and counter attack while the opponent is attacking.'
Should not have
• Do not include trite illustrations related to finance, money or investing.

```html
<!DOCTYPE html>
<html lang="en">
<head>
<meta charset="utf-8">
<title>Valtrimor LLC</title>
<link href="https://fonts.googleapis.com/css2?family=Jost:wght@400&family=Arimo:wght@400&display=swap" rel="stylesheet">
<style>
  :root {
    --hero-light: #b7cbe0;
    --hero-mid: #7f9dbd;
    --hero-dark: #1f3a5a;
    --rule-blue: #3176b5;
    --ink: #0a0a0a;
    --white: #ffffff;
    --panel-top: #d6d6d6;
    --panel-light: #f4f4f4;
    --heading-grey: #5a5a5a;
    --body-grey: #6e6e6e;
    --divider: #9a9a9a;
  }
  html, body {
    margin: 0;
    padding: 0;
    width: 1200px;
    height: 1000px;
    overflow: hidden;
  }
  .page {
    position: relative;
    width: 1200px;
    height: 1000px;
    overflow: hidden;
    background: radial-gradient(ellipse at 100% 70%, var(--panel-light) 0%, var(--panel-top) 60%);
  }
  .hero {
    position: absolute;
    left: 0; top: 0;
    width: 1200px; height: 642px;
    background:
      linear-gradient(100deg, rgba(255,255,255,0) 40%, rgba(31,58,90,0.75) 75%, rgba(20,45,75,0.9) 100%),
      linear-gradient(180deg, var(--hero-light) 0%, var(--hero-mid) 55%, var(--hero-dark) 100%);
  }
  .hero-rule {
    position: absolute;
    left: 0; top: 642px;
    width: 1200px; height: 1px;
    background: var(--rule-blue);
  }
  .brand {
    position: absolute;
    left: 113px; top: 190px;
    display: flex;
    align-items: center;
    gap: 12px;
  }
  .brand-mark {
    width: 55px; height: 55px;
    background: var(--ink);
  }
  .brand-name {
    font-family: "Jost", sans-serif;
    font-weight: 400;
    font-size: 58px;
    line-height: 1;
    letter-spacing: 1px;
    color: var(--ink);
  }
  .tagline {
    position: absolute;
    left: 113px; top: 542px;
    width: 900px;
    margin: 0;
    font-family: "Jost", sans-serif;
    font-size: 21px;
    line-height: 30px;
    color: var(--white);
  }
  .info {
    position: absolute;
    top: 678px; left: 0;
    width: 1200px;
  }
  .info-col {
    position: absolute;
    top: 0;
  }
  .info-col h2 {
    margin: 0 0 18px;
    font-family: "Arimo", sans-serif;
    font-weight: 400;
    font-size: 16px;
    line-height: 22px;
    color: var(--heading-grey);
  }
  .info-col p {
    margin: 0;
    font-family: "Arimo", sans-serif;
    font-size: 12px;
    line-height: 18px;
    color: var(--body-grey);
  }
  .col-about { left: 112px; width: 295px; }
  .col-focus { left: 528px; width: 300px; }
  .col-contact { left: 931px; }
  .divider {
    position: absolute;
    top: 0;
    width: 1px; height: 23px;
    background: var(--divider);
  }
</style>
</head>
<body>
<main class="page">
  <section class="hero" role="img" aria-label="Blurred photograph of a boardroom table with rows of office chairs in blue tones"></section>
  <div class="hero-rule"></div>

  <div class="brand">
    <div class="brand-mark"></div>
    <span class="brand-name">VALTRIMOR</span>
  </div>

  <p class="tagline">Lorem Ipsum is simply dummy text of the printing and typesetting industry. Lorem Ipsum has been the industry's standard dummy</p>

  <section class="info">
    <div class="info-col col-about">
      <h2>Lorem Ipsum is simply dummy text</h2>
      <p>Lorem Ipsum is simply dummy text of the printing and typesetting industry. Lorem Ipsum has been the indus-try's standard dummy text</p>
    </div>
    <div class="divider" style="left:448px"></div>
    <div class="info-col col-focus">
      <h2>Lorem Ipsum is simply dummy text</h2>
      <p>Lorem Ipsum is simply dummy text of the printing and typesetting industry.</p>
    </div>
    <div class="divider" style="left:876px"></div>
    <div class="info-col col-contact">
      <h2>info@example.com</h2>
    </div>
  </section>
</main>
</body>
</html>
```